New cookbook recipes app with New Technology Devices

App description:
Main features description that differentiates it from the current apps on the market:
Beautiful recipe cookbook app -> great look&feel and great UX;
Mise en Place Tab (Sort/Setup) -> Instead to have only the ingredients and the steps to cook Tab this new/different tab will help the cook to get all ingredients(raw or pre-cooked) organized and in order to be used on the recipe. This is a game changer in the cook learn-process.
Will change/present/show a different concept for measure/count quantities. Instead of display only the cups/pinch/time-to-cook/table-spoon etc (non-precision units), will have all these units converted in grams/pounds and cook internal temperatures.

Other features:
The app will work in all devices (phones, tablets, and desktops);
Good search tool by category or term filtration system;
No ads on the app (will be a subscription fee monetization method);
Inside the recipe the app will show the quantities in the usual way (spoons, pinches, and others) and new way (grams or lb);
Serving change capability (e.g. Serving for 2 persons can change to 4 people and the app will calculate the ingredients for that);
Pixolune and social media share capability;
If the user is logged in, the favorites will be enabled (user can save their fav recipes);
The app will allow recording videos and photos of the making process to share on social media.

Result expected:
I need a non-workable app, showing the app Design and Flow, to work on Tablets and Phones.

Target Market(s)

Cooks, average people looking for new technologies to cook

Font styles to use
Serif
Sans Serif

Requirements
Must have
• Great look and feel.
Serving change capability and unit conversion
Should not have
• Ads on the app

```html
<!DOCTYPE html>
<html lang="en">
<head>
<meta charset="utf-8">
<title>Filters</title>
<link rel="stylesheet" href="https://fonts.googleapis.com/css2?family=Poppins:wght@400;600;700&display=swap">
<style>
  :root {
    --brand-red: #c1343f;
    --brand-red-dark: #a92a35;
    --text-dark: #2b2b2b;
    --text-muted: #555555;
    --surface: #ffffff;
    --pattern-tint: #fbeff0;
  }
  * { box-sizing: border-box; margin: 0; padding: 0; }
  html, body {
    width: 813px; height: 1200px; overflow: hidden;
    background: var(--surface);
    font-family: "Poppins", sans-serif;
  }
  .screen { position: relative; width: 813px; height: 1200px; background: var(--surface); }

  .app-header {
    position: absolute; top: 0; left: 0; width: 100%; height: 160px;
    background: var(--brand-red);
    display: flex; align-items: center; justify-content: center;
  }
  .app-header__back { position: absolute; left: 28px; top: 64px; width: 30px; height: 30px; }
  .app-header__title {
    color: #fff; font-weight: 700; font-size: 42px; letter-spacing: 1px;
  }

  .background-pattern {
    position: absolute; top: 160px; left: 0; width: 100%; height: 920px;
    background: radial-gradient(circle at 60% 55%, var(--pattern-tint) 0%, rgba(255,255,255,0) 70%);
  }

  .filter-group { position: absolute; left: 0; width: 100%; }
  .filter-group__title {
    position: absolute; left: 26px; top: 0;
    font-weight: 700; font-size: 28px; color: var(--text-dark);
  }
  .option {
    position: absolute; display: flex; align-items: center; gap: 16px;
    font-size: 21px; color: var(--text-muted);
  }
  .option__box {
    width: 20px; height: 20px; border: 2px solid var(--brand-red); border-radius: 2px;
    display: flex; align-items: center; justify-content: center; flex-shrink: 0;
  }
  .option__box--checked { background: var(--brand-red); }
  .col-1 { left: 50px; } .col-2 { left: 335px; } .col-3 { left: 594px; }

  .tab-bar {
    position: absolute; bottom: 0; left: 0; width: 100%; height: 120px;
    background: var(--brand-red);
    display: flex; justify-content: space-around; align-items: center; padding: 0 40px;
  }
  .tab-bar svg { width: 52px; height: 52px; }
</style>
</head>
<body>
<div class="screen">
  <header class="app-header">
    <svg class="app-header__back" viewBox="0 0 30 30" aria-label="Back"><path d="M20 4 L9 15 L20 26" fill="none" stroke="#fff" stroke-width="4" stroke-linecap="round" stroke-linejoin="round"/></svg>
    <h1 class="app-header__title">FILTERS</h1>
  </header>

  <div class="background-pattern" role="img" aria-label="Faint line drawings of food and kitchen items"></div>

  <section class="filter-group" style="top:196px">
    <h2 class="filter-group__title">Cooking Time</h2>
    <label class="option col-1" style="top:66px"><span class="option__box"></span>&lt; 20 minutes</label>
    <label class="option col-2" style="top:66px"><span class="option__box"></span>20 - 40 minutes</label>
    <label class="option col-3" style="top:66px"><span class="option__box"></span>&gt; 40 minutes</label>
  </section>

  <section class="filter-group" style="top:328px">
    <h2 class="filter-group__title">Meal Type</h2>
    <label class="option col-1" style="top:66px"><span class="option__box"></span>Breakfast</label>
    <label class="option col-2" style="top:66px"><span class="option__box"></span>Lunch</label>
    <label class="option col-3" style="top:66px"><span class="option__box"></span>Dinner</label>
    <label class="option col-1" style="top:112px"><span class="option__box"></span>Snack</label>
    <label class="option col-2" style="top:112px"><span class="option__box"></span>Side Dish</label>
  </section>

  <section class="filter-group" style="top:506px">
    <h2 class="filter-group__title">Cuisines</h2>
    <label class="option col-1" style="top:76px"><span class="option__box"></span>American</label>
    <label class="option col-2" style="top:76px"><span class="option__box"></span>Asian</label>
    <label class="option col-3" style="top:76px"><span class="option__box"></span>Beverages</label>
    <label class="option col-1" style="top:123px"><span class="option__box"></span>Burgers</label>
    <label class="option col-2" style="top:123px"><span class="option__box"></span>Cakes &amp; Bakery</label>
    <label class="option col-3" style="top:123px"><span class="option__box"></span>Chicken</label>
    <label class="option col-1" style="top:170px"><span class="option__box"></span>Chinese</label>
    <label class="option col-2" style="top:170px"><span class="option__box option__box--checked"><svg width="14" height="14" viewBox="0 0 14 14"><path d="M2 7 L6 11 L12 3" fill="none" stroke="#fff" stroke-width="2.4"/></svg></span>Dessets</label>
    <label class="option col-3" style="top:170px"><span class="option__box"></span>Fast Food</label>
    <label class="option col-1" style="top:217px"><span class="option__box"></span>Filipino</label>
    <label class="option col-2" style="top:217px"><span class="option__box"></span>French</label>
    <label class="option col-3" style="top:217px"><span class="option__box"></span>Greek</label>
    <label class="option col-1" style="top:264px"><span class="option__box"></span>Halal</label>
    <label class="option col-2" style="top:264px"><span class="option__box"></span>Healthy</label>
    <label class="option col-3" style="top:264px"><span class="option__box"></span>Indian</label>
    <label class="option col-1" style="top:311px"><span class="option__box"></span>Indonesian</label>
    <label class="option col-2" style="top:311px"><span class="option__box"></span>Italian</label>
    <label class="option col-3" style="top:311px"><span class="option__box"></span>Japanese</label>
    <label class="option col-1" style="top:358px"><span class="option__box"></span>Korean</label>
    <label class="option col-2" style="top:358px"><span class="option__box"></span>Mexiacan</label>
    <label class="option col-3" style="top:358px"><span class="option__box"></span>Pizza</label>
    <label class="option col-1" style="top:405px"><span class="option__box"></span>Sandwiches</label>
    <label class="option col-2" style="top:405px"><span class="option__box"></span>Seafod</label>
    <label class="option col-3" style="top:405px"><span class="option__box"></span>Sushi</label>
    <label class="option col-1" style="top:452px"><span class="option__box"></span>Vegetarian</label>
    <label class="option col-2" style="top:452px"><span class="option__box"></span>Vietnamese</label>
    <label class="option col-3" style="top:452px"><span class="option__box"></span>Western</label>
  </section>

  <nav class="tab-bar">
    <svg viewBox="0 0 52 52" aria-label="Home"><path d="M8 26 L26 10 L44 26 H38 V42 H30 V32 H22 V42 H14 V26 Z" fill="#fff"/></svg>
    <svg viewBox="0 0 52 52" aria-label="Messages"><rect x="8" y="14" width="36" height="25" rx="3" fill="#fff"/><path d="M9 16 L26 29 L43 16" fill="none" stroke="var(--brand-red)" stroke-width="3"/></svg>
    <svg viewBox="0 0 52 52" aria-label="Add recipe"><circle cx="26" cy="26" r="18" fill="none" stroke="#fff" stroke-width="4"/><path d="M26 17 V35 M17 26 H35" stroke="#fff" stroke-width="4" stroke-linecap="round"/></svg>
    <svg viewBox="0 0 52 52" aria-label="Favorites"><path d="M26 43 L10 27 A9 9 0 0 1 26 15 A9 9 0 0 1 42 27 Z" fill="#fff"/></svg>
    <svg viewBox="0 0 52 52" aria-label="Profile"><circle cx="26" cy="26" r="18" fill="none" stroke="#fff" stroke-width="4"/><circle cx="26" cy="21" r="6" fill="#fff"/><path d="M14 38 C17 30 35 30 38 38" fill="#fff"/></svg>
  </nav>
</div>
</body>
</html>
```